Stationary design for real estate company in Trinidad and Tobago

Kestra Realty Ltd. , real estate company operating in Trinidad and Tobago, requires a sleek, modern and professional stationary package to wow our customers and potential new clients. we want to look sleek and professional; first impressions count in this business!
Business Address:
Level 1, Marlowe Point Tower
4C Seldon Grove Boulevard
Marlowe Point
Colwyn Pereira Highway
Port of Spain
Trinidad
Tel: + 1 868 555 0147
www.kestra-tt.com
info@kestra-tt.com

```html
<!DOCTYPE html>
<html lang="en">
<head>
<meta charset="utf-8">
<title>Kestra Realty Letterhead</title>
<link href="https://fonts.googleapis.com/css2?family=Questrial&family=Arimo:wght@400&display=swap" rel="stylesheet">
<style>
  :root {
    --navy: #1b365f;
    --navy-soft: #3a5580;
    --gold: #c59d5f;
    --ink: #555555;
    --rule: #9a9a9a;
    --backdrop: #e3e3e3;
    --paper: #ffffff;
  }
  * { margin: 0; padding: 0; box-sizing: border-box; }
  html, body { width: 1189px; height: 1200px; overflow: hidden; }
  body { background: var(--backdrop); position: relative; }

  .letterhead {
    position: absolute;
    left: 191px; top: 30px;
    width: 806px; height: 1140px;
    background: var(--paper);
    overflow: hidden;
  }
  .header-art { position: absolute; left: 0; top: 0; width: 420px; height: 240px; }

  .brand {
    position: absolute; left: 68px; top: 78px;
    display: flex; align-items: center; gap: 10px;
  }
  .brand-dot { width: 26px; height: 26px; border-radius: 50%; background: var(--gold); }
  .brand-name {
    font-family: "Questrial", sans-serif;
    font-size: 36px; color: var(--navy); letter-spacing: 1px;
  }

  .letter-body {
    position: absolute; left: 73px; top: 348px; width: 664px;
    font-family: "Arimo", Arial, sans-serif; color: var(--ink);
  }
  .salutation {
    font-family: "Questrial", sans-serif;
    font-size: 19px; font-weight: 700; margin-bottom: 30px;
  }
  .letter-body p.copy { font-size: 13.2px; line-height: 16.5px; margin-bottom: 15px; }
  .closing {
    font-family: "Questrial", sans-serif;
    font-size: 10.5px; font-weight: 700; margin-top: 30px;
  }
  .signature {
    width: 132px; height: 40px; margin-top: 30px;
    background: linear-gradient(90deg, #e6e6e6, #d8d8d8);
    border-radius: 4px;
  }

  .footer {
    position: absolute; left: 45px; top: 1062px; width: 716px;
    font-family: "Arimo", Arial, sans-serif; color: var(--ink);
    text-align: center;
  }
  .contact-row {
    display: flex; justify-content: center; align-items: center; gap: 14px;
    font-size: 12.5px; padding-bottom: 4px; border-bottom: 1px solid var(--rule);
  }
  .contact-item { display: flex; align-items: center; gap: 7px; }
  .contact-item svg { width: 10px; height: 10px; }
  .address { font-size: 12.3px; margin-top: 6px; white-space: nowrap; }
</style>
</head>
<body>
  <main class="letterhead">
    <svg class="header-art" viewBox="0 0 420 240" aria-hidden="true">
      <defs>
        <linearGradient id="navyFill" x1="0" y1="0" x2="1" y2="1">
          <stop offset="0" stop-color="#2a4670"/>
          <stop offset="1" stop-color="#1b365f"/>
        </linearGradient>
      </defs>
      <path d="M0 0 H408 C300 14 210 40 150 68 C80 110 30 170 0 232 Z" fill="var(--gold)"/>
      <path d="M0 0 H395 C290 14 205 38 146 64 C76 104 26 160 0 216 Z" fill="url(#navyFill)"/>
      <circle cx="108" cy="102" r="58" fill="var(--paper)"/>
    </svg>
    <rect role="img" aria-label="Faint world map texture within the navy corner band" style="display:none"></rect>

    <div class="brand">
      <span class="brand-dot"></span>
      <span class="brand-name">Kestra Realty</span>
    </div>

    <section class="letter-body">
      <p class="salutation">Dear Mr. Thorne,</p>
      <p class="copy">Lorem ipsum dolor sit amet, consectetuer adipiscing elit, sed diam nonmmy nibh euismod tincidunt ut laor eet dolore magna aliquam erat volutpat. Ut wisi enim ad minim veniam, quis nostrud exerci tationmcorper suscipit lobortis nisl ut aliquip ex ea commodo consequat. Duis autem vel eum iriure dolor in hendrerit in vulputate velit esse molestie consequat, vel illum dolore eu feugiat</p>
      <p class="copy">Rorem ipsum dolor sit amet, consectetuer adipiscing elit, sed diam nonmmy nibh euismod tincidunt ut laor eet dolore magna aliquam erat volutpat. Ut wisi enim ad minim veniam, quis nostrud exerci tationmcorper suscipit lobortis nisl ut aliquip ex ea commodo consequat. Duis autem vel eum iriure dolor in hendrerit in vulputate velit esse molest</p>
      <p class="copy">Dorem ipsum dolor sit amet, consectetuer adipiscing elit, sed diam nonmmy nibh euismod tincidunt ut laor eet dolore magna aliquam erat volutpat. Ut wisi enim ad minim veniam, quis nostrud exerci tationmcorper suscipit lobortis nisl ut aliquip ex ea commodo consequat. Duis autem vel eum iriure dolor in hendrerit in suscipit lobortis nisl ut aliquip ex ea commodo consequat. Duis autem vel eum iriure dolor in hendrerit in vulputate velit esse molestie consequat, vel illum</p>
      <p class="copy">Sorem ipsum dolor sit amet, consectetuer adipiscing elit, sed diam nonmmy nibh euismod tincidunt ut laor eet dolore magna aliquam erat volutpat. Ut wisi enim ad minim veniam, quis nostrud exerci tationmcorper suscipit lobortis nisl ut aliquip ex ea commodo consequat. Duis autem vel eum iriure dolor in</p>
      <p class="closing">Sincerely,</p>
      <div class="signature" role="img" aria-label="Handwritten signature of the sender"></div>
    </section>

    <footer class="footer">
      <div class="contact-row">
        <span class="contact-item">
          <svg viewBox="0 0 10 10"><path d="M2 0.5 L3.6 2.6 L2.7 3.6 C3.3 5 4.6 6.4 6.2 7.2 L7.3 6.3 L9.5 7.9 L8.4 9.5 C4.5 9 1 5.5 0.5 1.6 Z" fill="var(--gold)"/></svg>
          + 1 868 555 0147
        </span>
        <span class="contact-item">
          <svg viewBox="0 0 10 10"><circle cx="5" cy="5" r="4.2" fill="none" stroke="var(--gold)" stroke-width="1.4"/><path d="M1 5 H9 M5 1 C3 3 3 7 5 9 C7 7 7 3 5 1" fill="none" stroke="var(--gold)" stroke-width="1"/></svg>
          www.kestra-tt.com
        </span>
        <span class="contact-item">
          <svg viewBox="0 0 10 10"><rect x="0.5" y="2" width="9" height="6.5" fill="var(--gold)"/><path d="M0.5 2 L5 5.6 L9.5 2" fill="none" stroke="#fff" stroke-width="0.9"/></svg>
          info@kestra-tt.com
        </span>
      </div>
      <p class="address">Level 1, Marlowe Point Tower, 4C Seldon Grove Boulevard, Marlowe Point, Colwyn Pereira Highway, Port of Spain, Trinidad</p>
    </footer>
  </main>
</body>
</html>
```